Employment Agency Website Design

We are working with an employment agency in California.

Some sites to use for content/competitors and inspiration:

https://www.travinmoor.example/us/en
https://www.pelkoworksusa.example
https://www.dunmarhire.example
https://www.vantriga.example/en
https://www.ombrelusa.example
https://www.quilnstaffing.example

Thank you for taking the time to consider designing a website for us. We are web developers based in Stockton, CA, USA. Most of our projects go through the same process. Understanding this process may help you win a project with us. We custom-code all of our websites in-house. We don’t have any requirements as to what tools you use for your design, but we prefer Figma files. For any design that we label as four-stars, we send it to the client for review. The client picks the final design they want us to use. Once we complete this process, we will continue to show additional clients all the four-star sites and purchase them later. Your designs will have multiple chances to sell. For better chances of success, we ask that you follow these guidelines.

IMAGES:
If you use any images or icons in the design, we ask that you have a link to the asset so we can purchase the image/icon. Most of the designs we submit do not have the customer’s images on them unless they have some great images. Be creative; show us the feeling you are trying to portray with your image choices. Use any royalty-free site you choose. We subscribe to Adobe and mainly use their images, but we can purchase images outside of Adobe. PLEASE NOTE: we will not submit designs to clients with watermarks on the images.

FONTS:
We ask that you identify the fonts used in the design. This can be done in a message if you want. We typically use Google Fonts and Adobe Fonts.

CONTENT:
We're always open to different content and ideas. We often submit designs with stock images so the client can see our vision. We typically take pictures after the website launch to use their images with our vision. Lorem Ipsum is fine for paragraphs, but we ask that you write the headers in correct English. We want to be able to show the vision and identify the sections of the website.

INSPIRATION:
We typically add a couple of links in the brief of websites we like to help you get started in your design.

REVISIONS:
We do not often ask for revisions of the designs unless we see something in the design that may not appeal to the client. If there are slight changes that we want to make, we do that in the development process.

FEEDBACK:
We rarely give feedback on designs during the design process. We are working on many website projects and do not have the time to provide feedback. We usually respond if your request is well thought out and asks specific questions, but a note asking “feedback, please” usually goes unanswered.

```html
<!DOCTYPE html>
<html lang="en">
<head>
<meta charset="utf-8">
<title>Corvane Talent — Employment Agency</title>
<link href="https://fonts.googleapis.com/css2?family=Inter:wght@400;500;600;700;800&display=swap" rel="stylesheet">
<style>
:root{
  --red:#e0131f;
  --dark:#141414;
  --ink:#1b1b1b;
  --muted:#5a5a5a;
  --bg:#f4f4f4;
  --band:#e8e8e8;
  --white:#ffffff;
  --line:#c9c9c9;
}
*{box-sizing:border-box;margin:0;padding:0}
html,body{width:1200px;height:5133px;overflow:hidden}
body{font-family:'Inter',sans-serif;background:var(--bg);color:var(--ink);position:relative}
.abs{position:absolute}
h1,h2{font-weight:800;letter-spacing:-2px;line-height:1.02;text-transform:uppercase}

/* hero */
.hero{left:0;top:0;width:1200px;height:580px;background:linear-gradient(120deg,#3a2c24 0%,#6b5446 35%,#8a7566 60%,#4b3a30 100%)}
.hero-shade{left:0;top:0;width:1200px;height:580px;background:linear-gradient(90deg,rgba(0,0,0,.45),rgba(0,0,0,.05))}
.brand{display:flex;align-items:center;gap:8px;font-weight:600;color:var(--white);font-size:24px}
.brand-dot{width:22px;height:22px;border-radius:50%;background:var(--red)}
.nav-links{left:318px;top:40px;display:flex;gap:34px;font-size:13px;color:var(--white)}
.btn{display:flex;align-items:center;justify-content:center;border-radius:6px;font-size:13px;font-weight:500}
.btn-red{background:var(--red);color:var(--white)}
.btn-ghost{border:1.5px solid var(--white);color:var(--white)}
.hero h1{left:42px;top:172px;font-size:70px;color:var(--white)}
.hero-label{font-size:15px;color:var(--white)}
.field{height:38px;border:1px solid rgba(255,255,255,.6);border-radius:6px;color:rgba(255,255,255,.85);font-size:13px;display:flex;align-items:center;gap:8px;padding-left:10px}

/* jobs */
.jobs-title{left:42px;top:700px;font-size:72px}
.tabs{left:42px;top:880px;display:flex;align-items:center;font-size:15px;font-weight:600}
.tab{width:180px;height:48px;display:flex;align-items:center;justify-content:center;gap:6px}
.tab.active{background:var(--dark);color:var(--white);border-radius:12px}
.card{width:362px;height:234px;background:var(--dark);border-radius:10px;color:var(--white)}
.card-co{position:absolute;left:24px;top:34px;display:flex;align-items:center;gap:12px;font-size:12px;font-weight:600;text-transform:uppercase}
.card-co i{width:34px;height:34px;border-radius:6px;background:var(--white);display:block}
.card-role{position:absolute;left:24px;top:102px;font-size:19px;font-weight:500;text-transform:uppercase;white-space:nowrap;overflow:hidden;text-overflow:ellipsis;width:316px}
.card-loc{position:absolute;left:24px;top:178px;font-size:11px;color:#777}
.card-apply{position:absolute;right:24px;top:166px;width:90px;height:34px}
.load{left:535px;top:1474px;width:130px;height:34px;border:1.5px solid var(--ink);border-radius:8px;background:var(--white);font-size:12px}

/* talent */
.talent-title{left:24px;top:1668px;font-size:72px}
.talent-copy{left:24px;top:1905px;width:580px;font-size:12px;line-height:20px;color:var(--muted);text-transform:uppercase}
.form-label{font-size:16px;font-weight:500;line-height:24px}
.input{width:352px;height:40px;border:1.5px solid var(--line);border-radius:8px;background:var(--white);font-size:13px;color:#999;display:flex;align-items:center;padding-left:8px}
.chip{background:var(--white);border-radius:20px;box-shadow:0 2px 8px rgba(0,0,0,.15);font-size:12px;padding:8px 14px}

/* steps */
.steps-band{left:0;top:2388px;width:1200px;height:1544px;background:var(--band)}
.steps-title{left:0;top:2462px;width:1200px;text-align:center;font-size:72px}
.step-pill{height:96px;border:2px solid var(--ink);border-radius:48px;font-size:68px;font-weight:800;letter-spacing:-2px;display:flex;align-items:center;padding:0 20px}
.step-head{font-size:19px;font-weight:700;text-transform:uppercase}
.step-copy{font-size:12px;line-height:20px;color:var(--muted);text-transform:uppercase;width:490px}
.photo{border-radius:0}

/* articles */
.articles-title{left:0;top:4060px;width:1200px;text-align:center;font-size:72px}
.art-head{font-size:16px;font-weight:700;text-transform:uppercase}
.art-copy{font-size:12px;line-height:20px;color:var(--muted);text-transform:uppercase;width:350px}

/* footer */
.foot-brand{left:52px;top:4820px;display:flex;align-items:center;gap:14px;font-size:56px;color:var(--red);font-weight:500}
.foot-brand i{width:70px;height:70px;border-radius:50%;background:var(--red);display:block}
.foot-tag{left:140px;top:4890px;font-size:20px;color:var(--muted)}
.foot-links{left:42px;top:4960px;width:1116px;display:flex;justify-content:space-between;font-size:13px}
.foot-rule{left:42px;top:5008px;width:1116px;height:1px;background:var(--line)}
.socials{left:42px;top:5058px;display:flex;gap:14px}
.social{height:30px;border:1.5px solid var(--ink);border-radius:16px;font-size:12px;display:flex;align-items:center;padding:0 16px}
.copyright{right:52px;top:5066px;font-size:12px}
</style>
</head>
<body>

<!-- hero -->
<div class="abs hero" role="img" aria-label="Photo of three young professionals laughing around a laptop in a café"></div>
<div class="abs hero-shade"></div>
<div class="abs brand" style="left:44px;top:32px"><span class="brand-dot"></span>Corvane Talent</div>
<nav class="abs nav-links"><span>Home</span><span>Jobs</span><span>Hire Talent</span><span>Industries</span><span>Insights</span><span>About Us</span><span>Articles</span></nav>
<div class="abs btn btn-ghost" style="left:970px;top:31px;width:88px;height:36px">Sign In</div>
<div class="abs btn btn-red" style="left:1068px;top:31px;width:88px;height:36px">Sign Up</div>
<h1 class="abs">Push Your<br>Next Career</h1>
<div class="abs hero-label" style="left:42px;top:356px">Search Jobs Through Corvane Talent</div>
<div class="abs hero-label" style="left:408px;top:356px">Where ?</div>
<div class="abs field" style="left:42px;top:385px;width:350px">
  <svg width="14" height="14" viewBox="0 0 14 14"><circle cx="6" cy="6" r="4.5" fill="none" stroke="#fff" stroke-width="1.6"/><path d="M9.5 9.5L13 13" stroke="#fff" stroke-width="1.6"/></svg>Job Title</div>
<div class="abs field" style="left:408px;top:385px;width:350px">
  <svg width="14" height="16" viewBox="0 0 14 16"><path d="M7 1a5 5 0 0 0-5 5c0 4 5 9 5 9s5-5 5-9a5 5 0 0 0-5-5z" fill="#fff"/><circle cx="7" cy="6" r="2" fill="#555"/></svg>Location</div>
<div class="abs btn btn-red" style="left:776px;top:386px;width:144px;height:38px">Search Job</div>

<!-- latest jobs -->
<h2 class="abs jobs-title">Find Latest Jobs<br>That Suit You</h2>
<div class="abs tabs">
  <div class="tab active">IT &amp; SOFTWARE</div>
  <div class="tab">DESIGN</div>
  <div class="tab">MARKETING</div>
  <div class="tab">MORE <svg width="14" height="12" viewBox="0 0 14 12"><path d="M1 6h11M8 2l4 4-4 4" fill="none" stroke="#1b1b1b" stroke-width="1.6"/></svg></div>
</div>

<div class="abs card" style="left:42px;top:970px"><div class="card-co"><i></i>Harbor Nest</div><div class="card-role">Senior Frontend Engineer</div><div class="card-loc">Jakarta, Indonesia</div><div class="btn btn-red card-apply">Apply</div></div>
<div class="abs card" style="left:419px;top:970px"><div class="card-co"><i></i>Harbor Nest</div><div class="card-role">Senior Backend Engineer</div><div class="card-loc">Jakarta, Indonesia</div><div class="btn btn-red card-apply">Apply</div></div>
<div class="abs card" style="left:796px;top:970px"><div class="card-co"><i></i>Harbor Nest</div><div class="card-role">Data Analyst</div><div class="card-loc">Jakarta, Indonesia</div><div class="btn btn-red card-apply">Apply</div></div>
<div class="abs card" style="left:42px;top:1222px"><div class="card-co"><i></i>Harbor Nest</div><div class="card-role">Information Security Specialist</div><div class="card-loc">Jakarta, Indonesia</div><div class="btn btn-red card-apply">Apply</div></div>
<div class="abs card" style="left:419px;top:1222px"><div class="card-co" style="top:44px"><i></i>Harbor Nest</div><div class="card-role" style="top:112px">Network System Administrator</div><div class="card-loc" style="left:0;width:362px;text-align:center">Jakarta, Indonesia</div></div>
<div class="abs card" style="left:796px;top:1222px"><div class="card-co"><i></i>Harbor Nest</div><div class="card-role">Mobile App Developer</div><div class="card-loc">Jakarta, Indonesia</div><div class="btn btn-red card-apply">Apply</div></div>
<div class="abs btn load">Load More Job</div>

<!-- quality talent -->
<h2 class="abs talent-title">Find Quality<br>Talent For Your<br>Company</h2>
<p class="abs talent-copy">Give your company an edge in recruiting by finding the best talent in California. Our platform provides instant access to a network of high-quality job seekers from various industries. Explore potential candidates that fit your company's needs and create a successful team with us.</p>
<div class="abs form-label" style="left:22px;top:2020px">Find Candidates With Specific Specialties,<br>Experience Levels, Or Skills</div>
<div class="abs input" style="left:22px;top:2076px">Job Title</div>
<div class="abs form-label" style="left:22px;top:2134px">For A Role Located In</div>
<div class="abs input" style="left:22px;top:2166px">City</div>
<div class="abs btn btn-red" style="left:22px;top:2222px;width:168px;height:40px;font-size:12px">Search Candidates</div>

<div class="abs" style="left:672px;top:1640px;width:480px;height:552px;border:1.5px solid var(--line);border-radius:24px;transform:rotate(3deg);background:var(--white)"></div>
<div class="abs" role="img" aria-label="Red house-shaped backdrop with a young recruiter holding a tablet" style="left:694px;top:1640px;width:484px;height:552px;background:linear-gradient(160deg,#f0232d 0%,#c80d18 70%,#8f8f8f 100%);clip-path:polygon(50% 0,100% 36%,96% 100%,14% 100%,0 45%)"></div>
<div class="abs chip" style="left:756px;top:1838px">Organization</div>
<div class="abs chip" style="left:664px;top:1880px">Team Empowerment</div>
<div class="abs chip" style="left:688px;top:1924px">Communication</div>
<div class="abs chip" style="left:730px;top:1968px">Auditing</div>
<div class="abs" style="left:1000px;top:1796px;width:170px;height:110px;background:var(--white);border-radius:12px;box-shadow:0 4px 12px rgba(0,0,0,.15);padding:12px 18px;font-size:12px;line-height:26px"><b>Derek M</b><br>Certified TRX-CA<br>10+ Years Experience<br>California</div>
<div class="abs" style="left:888px;top:2100px;width:266px;height:72px;background:var(--white);border-radius:10px;box-shadow:0 4px 12px rgba(0,0,0,.15);padding:10px 22px">
  <div style="font-size:19px">Recruiter</div>
  <svg width="130" height="22" viewBox="0 0 130 22" fill="#f4b400"><g id="s"><path d="M10 1l2.7 6 6.3.6-4.8 4.3 1.4 6.3L10 15l-5.6 3.2 1.4-6.3L1 7.6l6.3-.6z"/></g><use href="#s" x="26"/><use href="#s" x="52"/><use href="#s" x="78"/><use href="#s" x="104"/></svg>
</div>

<!-- steps -->
<div class="abs steps-band"></div>
<h2 class="abs steps-title">How To Find Your<br>Dream Job Easily</h2>

<div class="abs step-pill" style="left:76px;top:2740px">STEP 1</div>
<div class="abs step-head" style="left:76px;top:2864px">Self-Understanding And Career Goals</div>
<p class="abs step-copy" style="left:76px;top:2910px">In pursuing your dream job, the first step is to identify your passions and skills, then set long-term career goals, and take an inventory of your personal values and priorities. In this way, you can form a solid foundation for your job search that suits your aspirations and needs.</p>
<div class="abs photo" role="img" aria-label="Photo of colleagues discussing ideas at a whiteboard in a bright office" style="left:600px;top:2685px;width:558px;height:377px;background:linear-gradient(135deg,#d9dde2,#9aa3ad 60%,#4a4f57)"></div>

<div class="abs photo" role="img" aria-label="Photo of a team working on laptops in a dim open-plan office" style="left:42px;top:3062px;width:558px;height:378px;background:linear-gradient(135deg,#3c3833,#7a6f63 50%,#2b2825)"></div>
<div class="abs step-pill" style="left:634px;top:3128px">STEP 2</div>
<div class="abs step-head" style="left:634px;top:3252px">Industry Research And Job Opportunities</div>
<p class="abs step-copy" style="left:634px;top:3298px">Pay attention to industry trends, find positions that match your qualifications and interests, and build a professional network. With these steps, you can increase your chances of finding a suitable job and support your career development.</p>

<div class="abs step-pill" style="left:76px;top:3516px">STEP 3</div>
<div class="abs step-head" style="left:76px;top:3640px">Active Applications And Opportunities</div>
<p class="abs step-copy" style="left:76px;top:3686px">Tailor your resume, take advantage of online networking, and prepare for interviews. With these steps, you'll be ready to face your job search journey with more confidence.</p>
<div class="abs photo" role="img" aria-label="Photo of a woman writing on sticky notes on a glass wall" style="left:600px;top:3440px;width:558px;height:378px;background:linear-gradient(135deg,#cfd3d6,#8e959b 55%,#3e4246)"></div>

<!-- articles -->
<h2 class="abs articles-title">An In-Depth Look At<br>Career Success</h2>
<div class="abs" role="img" aria-label="Photo of a developer coding at a desk with two monitors" style="left:42px;top:4240px;width:362px;height:276px;background:linear-gradient(135deg,#2a2e33,#6b6f74 55%,#1e2226)"></div>
<div class="abs" role="img" aria-label="Photo of two business people shaking hands over a desk" style="left:419px;top:4240px;width:362px;height:276px;background:linear-gradient(135deg,#e3e1dc,#a9a49c 55%,#5b5650)"></div>
<div class="abs" role="img" aria-label="Photo of a smiling senior professional woman in an office" style="left:796px;top:4240px;width:362px;height:276px;background:linear-gradient(135deg,#d6d8da,#9a9c9f 55%,#3f4144)"></div>
<div class="abs art-head" style="left:42px;top:4540px">What Jobs Are In Demand?</div>
<p class="abs art-copy" style="left:42px;top:4572px">Explore our demand for skilled talent report to see what specializations employers need most.</p>
<div class="abs art-head" style="left:419px;top:4540px">2024 Salary Guide</div>
<p class="abs art-copy" style="left:419px;top:4572px">Explore the latest data for 500-plus positions and know what you should earn or pay in local and national markets.</p>
<div class="abs art-head" style="left:796px;top:4540px">Multigenerational Workforce Report</div>
<p class="abs art-copy" style="left:796px;top:4572px">Learn how to better recruit, motivate and retain today's professionals at every age and stage of their careers.</p>

<!-- footer -->
<div class="abs foot-brand"><i></i>Corvane Talent</div>
<div class="abs foot-tag">The future of work.</div>
<nav class="abs foot-links"><span>Home</span><span>Jobs</span><span>Hire Talent</span><span>Industries</span><span>Insights</span><span>About Us</span><span>Articles</span><span>Articles</span><span>Sign Up</span><span>Privacy Policy</span><span>Terms of use</span></nav>
<div class="abs foot-rule"></div>
<div class="abs socials"><span class="social">Snapwell</span><span class="social">Friendwall</span><span class="social">Linkroll</span><span class="social">Viewtube</span></div>
<div class="abs copyright">© 2024 CORVANE TALENT. | ALL RIGHTS RESERVED.</div>

</body>
</html>
```